Business Card for a recruitment agency specializing in engineers and geeks.

I am looking to create Business Card Design for my company.
That
## Company name:
Quorvant Inc.
Quorvant is a term coined from the following concepts.
1. geek + engineer
2. geek utopia
## Company Description:
The concept of the company is to be a recruitment agency that creates a paradise for geeky engineers. We want to be a place where engineers can have more freedom and ideal career support.
# Target.
The noun itself is often given to companies that want to hire engineers, geeks, and IT-related personnel, so it would be nice to get the impression that this company seems to have good engineers and IT personnel. There are many occasions where I meet with the human resources department, president, or senior management and give it to them.
# Atmosphere
We are happy with simplicity, but with an impact that will help people remember the company. The logo is based on a dinosaur that does programming, so it should be somewhat playful, but since it will basically be used in a business setting, please don't make it too silly.
# About the logo
See the attached files. The company logo represents our engineers smiling upward because of our work, with the motif of a dinosaur doing programming.
## Color
We will leave the color scheme to you, but since the logo is in black and white, colors with such a taste would fit well.
## file format
ai, psd, png, svg
Industry/Entity Type
human resource and employment agency
Contact Information for Business Card
Company name, address, email, tel, URL,logo
Colors
Designer to choose colors to be used in the design.

```html
<!DOCTYPE html>
<html lang="en">
<head>
<meta charset="utf-8">
<title>Quorvant Inc. — Business Card</title>
<link rel="stylesheet" href="https://fonts.googleapis.com/css2?family=Poppins:wght@500;600;700&family=Roboto:wght@400&display=swap">
<style>
  :root{
    --magenta:#b0134f;
    --blue:#5aaee0;
    --orange:#f28c1c;
    --red:#d8283c;
    --ink:#111111;
    --white:#ffffff;
    --grey-dark:#4a4a4a;
    --page:#ffffff;
  }
  html,body{margin:0;padding:0;overflow:hidden;}
  body{width:874px;height:1200px;background:var(--page);position:relative;font-family:"Roboto",sans-serif;}
  .side-label{position:absolute;left:2px;font-family:"Roboto",sans-serif;font-size:22px;color:var(--ink);}
  .side-label--front{top:220px;}
  .side-label--back{top:918px;}
  .card{position:absolute;left:87px;width:787px;background:var(--white);overflow:hidden;}
  .card--front{top:44px;height:422px;}
  .card--back{top:743px;height:437px;}
  .card__shapes{position:absolute;inset:0;width:100%;height:100%;}
  .brand-front{position:absolute;left:28px;top:150px;display:flex;align-items:center;gap:10px;}
  .brand-front__mark{width:14px;height:14px;background:var(--white);}
  .brand-front__name{font-family:"Poppins",sans-serif;font-weight:600;font-size:34px;color:var(--white);}
  .company-title{position:absolute;left:388px;top:100px;margin:0;font-family:"Poppins",sans-serif;font-weight:600;font-size:36px;line-height:1.2;color:var(--ink);white-space:nowrap;}
  .pixel-accent{position:absolute;left:650px;top:10px;width:58px;height:52px;background:linear-gradient(135deg,var(--magenta),var(--blue) 60%,var(--orange));opacity:.8;}
  .contact-list{position:absolute;left:345px;top:252px;margin:0;padding:0;list-style:none;}
  .contact-list__item{display:flex;align-items:center;gap:9px;height:34px;font-size:13px;color:var(--ink);white-space:nowrap;}
  .contact-list__icon{width:24px;height:24px;border-radius:5px;display:flex;align-items:center;justify-content:center;flex:none;}
  .contact-list__icon svg{width:15px;height:15px;}
  .icon--address{background:var(--magenta);}
  .icon--email{background:var(--blue);}
  .icon--tel{background:var(--red);}
  .icon--web{background:var(--orange);}
  .code-panel{position:absolute;right:0;top:318px;width:134px;height:76px;background:linear-gradient(100deg,rgba(74,74,74,0),var(--grey-dark) 55%);clip-path:polygon(0 40%,100% 0,100% 100%,20% 100%);}
  .brand-back{position:absolute;left:0;right:0;top:230px;display:flex;justify-content:center;align-items:center;gap:12px;}
  .brand-back__mark{width:18px;height:18px;background:var(--magenta);}
  .brand-back__name{font-family:"Poppins",sans-serif;font-weight:600;font-size:42px;color:var(--magenta);}
  .pixel-accent--back{left:420px;top:120px;width:50px;height:46px;}
</style>
</head>
<body>
  <div class="side-label side-label--front">Front</div>
  <div class="side-label side-label--back">Back</div>

  <section class="card card--front">
    <svg class="card__shapes" viewBox="0 0 787 422" preserveAspectRatio="none" aria-hidden="true">
      <path d="M262,0 C330,120 360,260 320,422 L296,422 C330,260 304,120 242,0 Z" fill="var(--orange)"/>
      <path d="M236,0 C298,120 320,260 282,422 L262,422 C294,260 274,120 220,0 Z" fill="var(--blue)"/>
      <path d="M0,0 H212 C262,120 280,260 250,422 H0 Z" fill="var(--magenta)"/>
    </svg>
    <div class="brand-front">
      <span class="brand-front__mark"></span>
      <span class="brand-front__name">Quorvant</span>
    </div>
    <div class="pixel-accent" role="img" aria-label="Small pixel and code-tag accent"></div>
    <h1 class="company-title">Quorvant Inc.</h1>
    <ul class="contact-list">
      <li class="contact-list__item"><span class="contact-list__icon icon--address"><svg viewBox="0 0 24 24"><path d="M12 2a7 7 0 0 0-7 7c0 5 7 13 7 13s7-8 7-13a7 7 0 0 0-7-7zm0 9.5A2.5 2.5 0 1 1 12 6.5a2.5 2.5 0 0 1 0 5z" fill="#fff"/></svg></span>( Adress = Your adress here /)</li>
      <li class="contact-list__item"><span class="contact-list__icon icon--email"><svg viewBox="0 0 24 24"><path d="M3 6h18v12H3z" fill="none" stroke="#fff" stroke-width="2"/><path d="M3 6l9 7 9-7" fill="none" stroke="#fff" stroke-width="2"/></svg></span>( Email = Your E-mail adress here /)</li>
      <li class="contact-list__item"><span class="contact-list__icon icon--tel"><svg viewBox="0 0 24 24"><path d="M6.6 10.8a15 15 0 0 0 6.6 6.6l2.2-2.2a1 1 0 0 1 1-.25 11.4 11.4 0 0 0 3.6.57 1 1 0 0 1 1 1V20a1 1 0 0 1-1 1A17 17 0 0 1 3 4a1 1 0 0 1 1-1h3.5a1 1 0 0 1 1 1c0 1.25.2 2.45.57 3.6a1 1 0 0 1-.25 1z" fill="#fff"/></svg></span>( Tel = Your phone number here /)</li>
      <li class="contact-list__item"><span class="contact-list__icon icon--web"><svg viewBox="0 0 24 24"><circle cx="12" cy="12" r="9" fill="none" stroke="#fff" stroke-width="2"/><path d="M3 12h18M12 3c3 3 3 15 0 18M12 3c-3 3-3 15 0 18" fill="none" stroke="#fff" stroke-width="1.5"/></svg></span>( WebSite = Your website URL here /)</li>
    </ul>
    <div class="code-panel" role="img" aria-label="Decorative dark code-snippet graphic"></div>
  </section>

  <section class="card card--back">
    <svg class="card__shapes" viewBox="0 0 787 437" preserveAspectRatio="none" aria-hidden="true">
      <path d="M88,10 C150,140 158,300 104,437 L86,437 C136,300 128,140 70,10 Z" fill="var(--orange)"/>
      <path d="M64,0 C118,140 124,300 76,437 L60,437 C104,300 100,140 48,0 Z" fill="var(--blue)"/>
      <path d="M0,0 H40 C88,140 92,300 48,437 H0 Z" fill="var(--magenta)"/>
      <path d="M700,40 C620,160 612,300 680,430 L700,430 C636,300 642,160 716,40 Z" fill="var(--orange)"/>
      <path d="M724,30 C648,160 642,300 704,437 L722,437 C664,300 668,160 740,30 Z" fill="var(--blue)"/>
      <path d="M787,0 H760 C676,150 670,300 740,437 H787 Z" fill="var(--magenta)"/>
    </svg>
    <div class="pixel-accent pixel-accent--back" role="img" aria-label="Small pixel and code-tag accent"></div>
    <div class="brand-back">
      <span class="brand-back__mark"></span>
      <span class="brand-back__name">Quorvant</span>
    </div>
  </section>
</body>
</html>
```